Need Help Rebranding My Food Blog

I have a Wordpress Food blog called BeetBuddies.com. Right now it has no life and is very bland. I am rebranding this site to a new named called, TheHoneyedDays.com. I would love to have a blog that is vibrant and full of life and personality.

One of my top priorities when a new visitor comes to my site is to quickly understand what the site is about (Gluten-free, dairy-free sweets that taste delicious).

I also want people to feel a connection with me when they come to the site.

Here are some other things that I'd like in the blog design...

1. Optin
My business is driven by adding people to my list so it is very important for me to have an optin front and center/ above-the-fold. See https://www.quietrevenuehub.com/ as an example. The headline that I would like is "Gluten-free & dairy-free sweets that actually taste good"

2. Vibrant/full life
The next important aspect of this blog is that it is vibrant. I like colors that remind me of a SUNSET. See attachments for logo and color scheme. Here's an example of a site I really like that is vibrant: http://www.mellowplateliving.com/

Also see Image titled: "Sample: Feeling". Notice the feeling you get from the image/brush strokes and how it feels light, breezy, and free spirited.

3. Food Images
The last important aspect for my blog is to showcase my recipes. I have attached a few of them as examples. Its really important for a food blog to showcase beautiful pictures of recipes for people to see so will definitely need this in the design.

Also, attached...
1. Image of me.
2. New logo for TheHoneyedDays (notice: don't use the one attached as "Sample/Feeling". That's just for reference of the feeling I like.)

Thanks!

Rosalind

P.S. I didn't include all the copy that would be needed so feel free to use the "lorem ipsum" text as placeholder if need be.

Target Market(s)

stay-at-home moms, dairy-free & gluten allergies, love desserts & sweets

Coding

Coded - Design and coding required

Font styles to use
Sans Serif

Requirements
Must have
• 1. Optin area with my picture and what I'm about ""Gluten-free & dairy-free sweets that actually taste good""
• 2. Must have personality/vibrancy to the site. Think full of life, not dull like my current website... beetbuddies.com
• 3. Highlight food images (Vertical image holders only)
Nice to have
• Color scheme should be based on my logo
Should not have
• No black or grey colors

```html
<!DOCTYPE html>
<html lang="en">
<head>
<meta charset="utf-8">
<title>TheHoneyedDays</title>
<link rel="stylesheet" href="https://fonts.googleapis.com/css2?family=Lora:ital,wght@1,600;1,700&family=Open+Sans:wght@400;600;700&display=swap">
<style>
:root{
  --pink:#de2d57;
  --pink-dark:#8c1b33;
  --orange:#e8843a;
  --orange-head:#ea5a3a;
  --yellow:#f8c21c;
  --yellow-light:#fbd34e;
  --lime:#b5cc18;
  --panel:#f4f4f4;
  --text:#3a2a2a;
  --muted:#6b5a55;
  --white:#ffffff;
}
*{box-sizing:border-box;margin:0;padding:0}
html,body{width:1200px;height:2264px;overflow:hidden;background:var(--white)}
body{position:relative;font-family:"Open Sans",sans-serif;color:var(--text)}
.script{font-family:"Lora",serif;font-style:italic;font-weight:700}

.site-header{position:absolute;left:0;top:0;width:1200px;height:131px;background:linear-gradient(90deg,#ea6a3c 0%,#e2405a 35%,#de2d57 100%)}
.brand-block{position:absolute;left:0;top:0;width:382px;height:131px;background:linear-gradient(90deg,#ec5f3a,#e3455a)}
.brand{position:absolute;left:133px;top:44px;font-family:"Lora",serif;font-style:italic;font-weight:700;font-size:30px;color:var(--white);letter-spacing:.3px}
.search{position:absolute;left:827px;top:24px;width:240px;height:39px;background:#8a1a34;border:1px solid #6e1229;color:#d88a9c;font-size:11px;padding:11px 14px}
.main-nav{position:absolute;top:89px;right:133px;display:flex;gap:38px}
.main-nav a{color:var(--white);text-decoration:none;font-size:17px}

.hero{position:absolute;left:133px;top:146px;width:679px;height:417px;background:linear-gradient(120deg,#c2d63a 0%,var(--lime) 45%,#98ad12 100%)}
.hero-title{position:absolute;left:256px;top:136px;font-size:37px;line-height:43px;color:var(--white)}
.hero-btn{position:absolute;left:256px;top:237px;width:96px;height:38px;background:var(--yellow);color:var(--pink-dark);font-size:11px;font-weight:700;display:flex;align-items:center;justify-content:center}
.hero-arrow{position:absolute;top:200px;width:18px;height:18px;border-radius:50%;border:1px solid rgba(255,255,255,.7);background:rgba(255,255,255,.2)}
.hero-arrow svg{display:block;margin:4px auto}

.post{position:absolute;left:133px;width:679px;height:279px;background:var(--panel)}
.post-photo{position:absolute;left:0;top:0;width:278px;height:279px}
.post-body{position:absolute;left:309px;top:34px;width:345px}
.post-title{font-size:17px;color:var(--pink);font-weight:400}
.post-by{font-size:11px;margin-top:6px;color:var(--text)}
.post-excerpt{font-size:11.5px;line-height:22.6px;margin-top:12px;color:var(--text)}
.post-meta{position:absolute;left:309px;top:225px;display:flex;gap:28px;font-size:11px;color:var(--muted)}
.post-meta span{display:flex;align-items:center;gap:6px}

.pager{position:absolute;left:133px;top:2077px;display:flex;gap:12px;align-items:center}
.pager span{width:28px;height:28px;border:1px solid #d8c8c0;display:flex;align-items:center;justify-content:center;font-size:12px;color:var(--text)}
.pager .gap{border:none;width:auto;letter-spacing:2px}

.optin{position:absolute;left:827px;top:146px;width:240px;height:254px;background:linear-gradient(135deg,var(--yellow) 0%,var(--yellow) 55%,var(--yellow-light) 55%,var(--yellow) 100%)}
.optin-title{position:absolute;left:16px;top:16px;width:215px;font-size:17px;line-height:21px;color:var(--pink-dark)}
.field{position:absolute;left:16px;width:209px;height:41px;background:var(--white);font-size:11px;color:#8a7a75;padding:13px 16px}
.signup{position:absolute;left:16px;top:195px;width:112px;height:39px;background:var(--pink);color:var(--white);font-size:11px;font-weight:700;display:flex;align-items:center;justify-content:center}

.side-heading{position:absolute;left:827px;font-size:17px;color:var(--pink)}
.mini{position:absolute;left:827px;width:240px;height:95px;background:var(--panel)}
.mini-photo{position:absolute;left:0;top:0;width:95px;height:95px}
.mini-title{position:absolute;left:115px;top:20px;width:110px;font-size:11px;line-height:19px;color:var(--text)}

.categories{position:absolute;left:827px;top:1625px;width:240px;height:280px;background:var(--panel);padding:14px 24px}
.categories li{list-style:none;font-size:13px;line-height:32px;color:var(--text)}

.site-footer{position:absolute;left:0;top:2169px;width:1200px;height:95px;background:var(--orange)}
.foot-links{position:absolute;left:133px;top:26px;font-size:11px;color:var(--text)}
.foot-copy{position:absolute;left:133px;top:52px;font-size:11px;color:var(--text)}
.social{position:absolute;right:133px;top:30px;display:flex;gap:8px}
.social span{width:35px;height:35px;border-radius:50%;background:var(--white)}
</style>
</head>
<body>

<header class="site-header">
  <div class="brand-block"></div>
  <div class="brand">TheHoneyedDays</div>
  <div class="search">Search</div>
  <nav class="main-nav script">
    <a>Home</a><a>About Us</a><a>Recipes</a><a>Resources</a>
  </nav>
</header>

<section class="hero" role="img" aria-label="Smiling blogger holding a plate of cake over a lime-tinted kitchen scene">
  <span class="hero-arrow" style="left:18px"><svg width="8" height="8" viewBox="0 0 8 8"><path d="M5 1 2 4l3 3" fill="none" stroke="#fff" stroke-width="1.3"/></svg></span>
  <span class="hero-arrow" style="left:642px"><svg width="8" height="8" viewBox="0 0 8 8"><path d="M3 1l3 3-3 3" fill="none" stroke="#fff" stroke-width="1.3"/></svg></span>
  <h1 class="hero-title script">Donec vestibulum<br>scelerisque diam mollis</h1>
  <div class="hero-btn">READ MORE</div>
</section>

<article class="post" style="top:580px">
  <div class="post-photo" role="img" aria-label="Stack of chocolate-glazed baked donuts" style="background:linear-gradient(160deg,#7a3a1a,#4a2010 60%,#f2ece6)"></div>
  <div class="post-body">
    <h2 class="post-title">Peanut Butter No Bake Energy Bites</h2>
    <p class="post-by">by Rosalind</p>
    <p class="post-excerpt">Let's face it, being a stay a home mom is rarely glamorous. Glam-our days for me now consist of straightening my hair and putting on jeans instead of yoga pants. Before the sun wakes up and until we fall asleep, someone is needing us. In fact, if you are a stay at home mom, than […]</p>
  </div>
  <div class="post-meta">
    <span><svg width="11" height="10" viewBox="0 0 11 10"><path d="M1 1h9v6H4L1 9z" fill="#6b5a55"/></svg>11 Comments</span>
    <span><svg width="10" height="10" viewBox="0 0 10 10"><circle cx="8" cy="2" r="1.6" fill="#6b5a55"/><circle cx="2" cy="5" r="1.6" fill="#6b5a55"/><circle cx="8" cy="8" r="1.6" fill="#6b5a55"/><path d="M8 2 2 5l6 3" fill="none" stroke="#6b5a55"/></svg>31 Shares</span>
    <span><svg width="10" height="10" viewBox="0 0 10 10"><circle cx="5" cy="5" r="4" fill="none" stroke="#6b5a55"/><circle cx="5" cy="5" r="1.5" fill="#6b5a55"/></svg>Read more</span>
  </div>
</article>

<article class="post" style="top:876px">
  <div class="post-photo" role="img" aria-label="Stack of oatmeal chocolate chip cookies" style="background:linear-gradient(160deg,#e8e6e2,#b07a3a 45%,#7a4a1e 75%,#d8d4cc)"></div>
  <div class="post-body">
    <h2 class="post-title">Peanut Butter No Bake Energy Bites</h2>
    <p class="post-by">by Rosalind</p>
    <p class="post-excerpt">Let's face it, being a stay a home mom is rarely glamorous. Glam-our days for me now consist of straightening my hair and putting on jeans instead of yoga pants. Before the sun wakes up and until we fall asleep, someone is needing us. In fact, if you are a stay at home mom, than […]</p>
  </div>
  <div class="post-meta">
    <span><svg width="11" height="10" viewBox="0 0 11 10"><path d="M1 1h9v6H4L1 9z" fill="#6b5a55"/></svg>11 Comments</span>
    <span><svg width="10" height="10" viewBox="0 0 10 10"><circle cx="8" cy="2" r="1.6" fill="#6b5a55"/><circle cx="2" cy="5" r="1.6" fill="#6b5a55"/><circle cx="8" cy="8" r="1.6" fill="#6b5a55"/><path d="M8 2 2 5l6 3" fill="none" stroke="#6b5a55"/></svg>31 Shares</span>
    <span><svg width="10" height="10" viewBox="0 0 10 10"><circle cx="5" cy="5" r="4" fill="none" stroke="#6b5a55"/><circle cx="5" cy="5" r="1.5" fill="#6b5a55"/></svg>Read more</span>
  </div>
</article>

<article class="post" style="top:1172px">
  <div class="post-photo" role="img" aria-label="Pumpkin dessert bites in a white ramekin beside small pumpkins" style="background:linear-gradient(170deg,#e88a2a,#c46a1e 40%,#e4e0d6 70%,#8a6a48)"></div>
  <div class="post-body">
    <h2 class="post-title">Peanut Butter No Bake Energy Bites</h2>
    <p class="post-by">by Rosalind</p>
    <p class="post-excerpt">Let's face it, being a stay a home mom is rarely glamorous. Glam-our days for me now consist of straightening my hair and putting on jeans instead of yoga pants. Before the sun wakes up and until we fall asleep, someone is needing us. In fact, if you are a stay at home mom, than […]</p>
  </div>
  <div class="post-meta">
    <span><svg width="11" height="10" viewBox="0 0 11 10"><path d="M1 1h9v6H4L1 9z" fill="#6b5a55"/></svg>11 Comments</span>
    <span><svg width="10" height="10" viewBox="0 0 10 10"><circle cx="8" cy="2" r="1.6" fill="#6b5a55"/><circle cx="2" cy="5" r="1.6" fill="#6b5a55"/><circle cx="8" cy="8" r="1.6" fill="#6b5a55"/><path d="M8 2 2 5l6 3" fill="none" stroke="#6b5a55"/></svg>31 Shares</span>
    <span><svg width="10" height="10" viewBox="0 0 10 10"><circle cx="5" cy="5" r="4" fill="none" stroke="#6b5a55"/><circle cx="5" cy="5" r="1.5" fill="#6b5a55"/></svg>Read more</span>
  </div>
</article>

<article class="post" style="top:1468px">
  <div class="post-photo" role="img" aria-label="Watermelon popsicle slices on a grey tray" style="background:linear-gradient(150deg,#e8524a,#8a8a8a 50%,#e85a4e)"></div>
  <div class="post-body">
    <h2 class="post-title">Peanut Butter No Bake Energy Bites</h2>
    <p class="post-by">by Rosalind</p>
    <p class="post-excerpt">Let's face it, being a stay a home mom is rarely glamorous. Glam-our days for me now consist of straightening my hair and putting on jeans instead of yoga pants. Before the sun wakes up and until we fall asleep, someone is needing us. In fact, if you are a stay at home mom, than […]</p>
  </div>
  <div class="post-meta">
    <span><svg width="11" height="10" viewBox="0 0 11 10"><path d="M1 1h9v6H4L1 9z" fill="#6b5a55"/></svg>11 Comments</span>
    <span><svg width="10" height="10" viewBox="0 0 10 10"><circle cx="8" cy="2" r="1.6" fill="#6b5a55"/><circle cx="2" cy="5" r="1.6" fill="#6b5a55"/><circle cx="8" cy="8" r="1.6" fill="#6b5a55"/><path d="M8 2 2 5l6 3" fill="none" stroke="#6b5a55"/></svg>31 Shares</span>
    <span><svg width="10" height="10" viewBox="0 0 10 10"><circle cx="5" cy="5" r="4" fill="none" stroke="#6b5a55"/><circle cx="5" cy="5" r="1.5" fill="#6b5a55"/></svg>Read more</span>
  </div>
</article>

<article class="post" style="top:1764px">
  <div class="post-photo" role="img" aria-label="Chocolate bark topped with pumpkin seeds and dried fruit" style="background:linear-gradient(160deg,#5a3a22,#3e2416 50%,#8a7a3a)"></div>
  <div class="post-body">
    <h2 class="post-title">Peanut Butter No Bake Energy Bites</h2>
    <p class="post-by">by Rosalind</p>
    <p class="post-excerpt">Let's face it, being a stay a home mom is rarely glamorous. Glam-our days for me now consist of straightening my hair and putting on jeans instead of yoga pants. Before the sun wakes up and until we fall asleep, someone is needing us. In fact, if you are a stay at home mom, than […]</p>
  </div>
  <div class="post-meta">
    <span><svg width="11" height="10" viewBox="0 0 11 10"><path d="M1 1h9v6H4L1 9z" fill="#6b5a55"/></svg>11 Comments</span>
    <span><svg width="10" height="10" viewBox="0 0 10 10"><circle cx="8" cy="2" r="1.6" fill="#6b5a55"/><circle cx="2" cy="5" r="1.6" fill="#6b5a55"/><circle cx="8" cy="8" r="1.6" fill="#6b5a55"/><path d="M8 2 2 5l6 3" fill="none" stroke="#6b5a55"/></svg>31 Shares</span>
    <span><svg width="10" height="10" viewBox="0 0 10 10"><circle cx="5" cy="5" r="4" fill="none" stroke="#6b5a55"/><circle cx="5" cy="5" r="1.5" fill="#6b5a55"/></svg>Read more</span>
  </div>
</article>

<nav class="pager">
  <span>«</span><span>1</span><span>2</span><span>3</span><span>4</span><span>5</span><span class="gap">......</span><span>18</span><span>»</span>
</nav>

<aside>
  <div class="optin">
    <p class="optin-title script">Gluten-free &amp; dairy-free sweets that actually taste good</p>
    <div class="field" style="top:92px">Name</div>
    <div class="field" style="top:142px">Email</div>
    <div class="signup">SIGN UP NOW</div>
  </div>

  <h3 class="side-heading script" style="top:436px">Recent Posts</h3>
  <div class="mini" style="top:468px"><div class="mini-photo" role="img" aria-label="Pink food coloring in a bowl" style="background:linear-gradient(135deg,#e88a9a,#c45a6a 60%,#d8c8a0)"></div><p class="mini-title">How to Make Pink Food Coloring Natu-rally Using Beets</p></div>
  <div class="mini" style="top:572px"><div class="mini-photo" role="img" aria-label="Bowl of creamy potato soup" style="background:linear-gradient(135deg,#f2ead0,#e8c86a 55%,#f4f0e8)"></div><p class="mini-title">Dairy-Free Creamy Potato Soup</p></div>
  <div class="mini" style="top:676px"><div class="mini-photo" role="img" aria-label="Cinnamon swirl popcorn in a bowl" style="background:linear-gradient(135deg,#e8d8c0,#c49a6a 50%,#d84a3a)"></div><p class="mini-title">Cinnamon Swirl Pop-corn</p></div>
  <div class="mini" style="top:780px"><div class="mini-photo" role="img" aria-label="Fruit-topped breakfast bowl on a patterned cloth" style="background:linear-gradient(135deg,#e8b83a,#6a4a8a 55%,#d8d0c0)"></div><p class="mini-title">Top 10 Best Recipes of 2016</p></div>
  <div class="mini" style="top:884px"><div class="mini-photo" role="img" aria-label="Orange soup in a round bowl" style="background:linear-gradient(135deg,#5a5a5a,#e8943a 45%,#c46a22)"></div><p class="mini-title">Dairy-free Pretzel Peppermint Choco-late Bark</p></div>

  <h3 class="side-heading script" style="top:1013px">Most Commented Posts</h3>
  <div class="mini" style="top:1045px"><div class="mini-photo" role="img" aria-label="Roasted carrots on a dark plate" style="background:linear-gradient(135deg,#2a2a22,#d86a2a 50%,#4a6a2a)"></div><p class="mini-title">How to Make Pink Food Coloring Natu-rally Using Beets</p></div>
  <div class="mini" style="top:1149px"><div class="mini-photo" role="img" aria-label="Glazed donuts on a white surface" style="background:linear-gradient(135deg,#5a2a1a,#e8a0b0 50%,#f0ece6)"></div><p class="mini-title">Dairy-Free Creamy Potato Soup</p></div>
  <div class="mini" style="top:1253px"><div class="mini-photo" role="img" aria-label="Bowl of popcorn with cinnamon sticks" style="background:linear-gradient(135deg,#a8c8c0,#f0e8dc 50%,#c47a4a)"></div><p class="mini-title">Cinnamon Swirl Pop-corn</p></div>
  <div class="mini" style="top:1357px"><div class="mini-photo" role="img" aria-label="Chocolate-dipped orange peels" style="background:linear-gradient(135deg,#3a2418,#e8843a 50%,#e8e0d8)"></div><p class="mini-title">Top 10 Best Recipes of 2016</p></div>
  <div class="mini" style="top:1461px"><div class="mini-photo" role="img" aria-label="Peppermint pretzel bark" style="background:linear-gradient(90deg,#c42a3a,#e8e0d0 30%,#6a8a3a 60%,#c42a3a)"></div><p class="mini-title">Dairy-free Pretzel Peppermint Choco-late Bark</p></div>

  <h3 class="side-heading script" style="top:1592px">Categories</h3>
  <ul class="categories">
    <li>Breakfast (12)</li><li>Dessert (22)</li><li>Dinner (16)</li><li>Lunch (11)</li><li>Resources (14)</li><li>Snack (19)</li><li>Uncategorized (1)</li><li>Vegan (28)</li>
  </ul>
</aside>

<footer class="site-footer">
  <p class="foot-links">Home &nbsp;&nbsp;|&nbsp;&nbsp; About Us &nbsp;&nbsp;|&nbsp;&nbsp; Recipes &nbsp;&nbsp;|&nbsp;&nbsp; Resources</p>
  <p class="foot-copy">Copyright &copy; 2017 &nbsp;Company name. &nbsp;All rights reserved.</p>
  <div class="social"><span></span><span></span><span></span><span></span><span></span><span></span></div>
</footer>

</body>
</html>
```